insert for clam shell / vape cartridge

Brand : Brevor (roman god of fire)
card insert dimensions are 2.5" in width and 3.375" in height
this is a cannabis product. Open to any and all designs. Currently using very generic text. 5/8" on left edge of design will be covered by the cartridge

Target Market(s)

medical cannabis patients

Industry/Entity Type

Product

Logo Text

Brevor

Requirements
Must have
• logo
Nice to have
• "distilled cannabis oil"
• "no pg/vg"
• subtle use of cannabis leaf
Should not have
• no big (prominent) Pot leaves

```html
<!DOCTYPE html>
<html lang="en">
<head>
<meta charset="utf-8">
<title>Vapor – Distilled Cannabis Oil Card Insert</title>
<link rel="stylesheet" href="https://fonts.googleapis.com/css2?family=Open+Sans:wght@600;700&family=Source+Serif+4:wght@700&display=swap">
<style>
  :root {
    --page: #ffffff;
    --leaf-green: #8dc63f;
    --amber: #fbb040;
    --sand: #d9bf8c;
    --sand-light: #efe3cb;
    --ink: #1f1f1f;
    --white: #ffffff;
    --seal: #1a1a1a;
  }
  * { box-sizing: border-box; margin: 0; padding: 0; }
  html, body {
    width: 1200px; height: 813px; overflow: hidden;
    background: var(--page);
  }
  .canvas { position: relative; width: 1200px; height: 813px; }

  .card {
    position: absolute; left: 370px; top: 86px;
    width: 474px; height: 644px; overflow: hidden;
  }
  .card__pattern {
    position: absolute; inset: 0;
    background: linear-gradient(135deg, var(--sand-light), #f6eedd 50%, var(--sand-light));
  }

  .logo-plate {
    position: absolute; left: 190px; top: 66px;
    width: 164px; height: 48px; background: var(--white);
    display: flex; align-items: center; justify-content: center;
    border-radius: 6px;
  }
  .logo-plate__text {
    font-family: "Source Serif 4", Georgia, serif; font-weight: 700;
    font-size: 28px; color: var(--leaf-green); letter-spacing: 0.3px;
  }

  .product-badge {
    position: absolute; left: 143px; top: 152px;
    width: 279px; height: 181px;
    border: 6px solid var(--leaf-green); border-radius: 16px;
    background: var(--white);
  }
  .product-badge__name {
    position: absolute; left: 0; right: 0; top: 14px;
    text-align: center;
    font-family: "Open Sans", Arial, sans-serif; font-weight: 700;
    font-size: 67px; line-height: 1; color: var(--leaf-green);
    letter-spacing: 1px;
  }
  .product-badge__band {
    position: absolute; left: 4px; right: 4px; top: 100px; height: 62px;
    background: var(--amber);
    border-radius: 0 0 12px 12px;
    display: flex; align-items: center; justify-content: center;
    padding-bottom: 12px;
  }
  .product-badge__tagline {
    font-family: "Open Sans", Arial, sans-serif; font-weight: 600;
    font-size: 16px; color: var(--white); letter-spacing: 0.2px;
  }

  .info-band {
    position: absolute; left: 0; top: 384px; width: 474px; height: 161px;
    background: var(--leaf-green);
    border-radius: 6px 0 0 4px;
  }
  .info-band__claim {
    position: absolute; right: 58px; top: 12px;
    font-family: "Source Serif 4", Georgia, serif; font-weight: 700;
    font-size: 16px; color: var(--white);
  }
  .info-band__seal {
    position: absolute; left: 344px; top: 54px;
  }

  .net-weight {
    position: absolute; left: 308px; top: 558px;
    width: 122px; height: 50px; background: var(--white);
    border-radius: 6px;
    display: flex; align-items: center; justify-content: center;
    font-family: "Source Serif 4", Georgia, serif; font-weight: 700;
    font-size: 27px; color: var(--ink);
  }
</style>
</head>
<body>
<main class="canvas">
  <section class="card">
    <div class="card__pattern" role="img" aria-label="Sand-coloured geometric striped cube pattern on white"></div>

    <div class="logo-plate"><span class="logo-plate__text">LOGO HERE</span></div>

    <div class="product-badge">
      <div class="product-badge__name">VAPOR</div>
      <div class="product-badge__band">
        <span class="product-badge__tagline">DISTILLED CANNABIS OIL</span>
      </div>
    </div>

    <div class="info-band">
      <p class="info-band__claim">NO PG or VG</p>
      <svg class="info-band__seal" width="74" height="74" viewBox="0 0 74 74" role="img" aria-label="Medical use seal">
        <circle cx="37" cy="37" r="36" fill="var(--seal)"/>
        <circle cx="37" cy="37" r="29" fill="none" stroke="var(--white)" stroke-width="2"/>
      </svg>
    </div>

    <div class="net-weight">1 gram</div>
  </section>
</main>
</body>
</html>
```